HR consultancy website - Wordpress Design Project

We need a wordpress design for a new company based in Belgium called Brivolane. We propose HR consultancy services focused on employees' engagement (motivation). We target corporations from 100 to 1000+ employees mainly in Europe.
We need a new design for our existing website (www.brivolane.eu).
We find the current design too static and outdated and we are looking for a more appealing look & feel.
Nevertheless, it has also to be sober.
The colours of the logo (dark blue, purple and light grey) should be preferrably used.
The content structure and the texts remain the same.

Target Market(s)

HR managers, general managers of SME's, higher education

Industry/Entity Type

It Company

Requirements
Must have
• No specific functionalities, except a contact form.

```html
<!DOCTYPE html>
<html lang="en">
<head>
<meta charset="utf-8">
<title>Brivolane – HR Engagement Consultancy</title>
<link href="https://fonts.googleapis.com/css2?family=Source+Sans+3:wght@400;600;700&family=Questrial&family=Open+Sans:wght@400;600&display=swap" rel="stylesheet">
<style>
:root{
  --pink:#ea2a7a;
  --ink:#4a4a4c;
  --paper:#fbfafb;
  --navy:#0b4a9a;
  --green:#5ac540;
  --footer:#1c1c1c;
  --chart-light:#e6f0fa;
  --chart-blue:#4f95d6;
}
*{margin:0;padding:0;box-sizing:border-box}
html,body{width:951px;height:1200px;overflow:hidden;background:var(--paper);font-family:"Source Sans 3",sans-serif}
.page{position:relative;width:951px;height:1200px;overflow:hidden}
.abs{position:absolute}

.site-header{left:0;top:0;width:951px;height:82px;background:#fff}
.brand{left:100px;top:28px;display:flex;align-items:center;gap:8px;font-family:"Questrial",sans-serif;font-size:26px;color:#c9c4c4;letter-spacing:1px}
.brand-dot{width:12px;height:12px;background:var(--navy)}
.main-nav{left:616px;top:30px;display:flex;gap:11px;font-family:"Open Sans",sans-serif;font-size:12px;font-weight:600;align-items:center}
.main-nav a{color:#555;text-decoration:none;padding:3px 4px}
.main-nav a.active{background:var(--navy);color:#fff;border-radius:3px;padding:3px 9px}
.main-nav a.faded{color:#aaa}

.hero{left:0;top:82px;width:951px;height:343px;background:linear-gradient(160deg,#ef3a86 0%,var(--pink) 60%,#e72577 100%);box-shadow:inset 0 6px 8px -4px rgba(0,0,0,.25)}
.hero-title{left:97px;top:132px;width:420px;font-size:28px;font-weight:700;color:#fff;line-height:29px;text-shadow:0 1px 2px rgba(0,0,0,.25)}
.hero-copy{left:97px;top:209px;width:392px;font-size:14px;line-height:19.3px;color:#fbd3e3}
.cta{left:95px;top:331px;width:230px;height:45px;background:linear-gradient(#71b3ea,#4d93d6);border:1px solid #3d7fc0;border-radius:2px;color:#fff;font-weight:700;font-size:17px;display:flex;align-items:center;justify-content:center;text-shadow:0 1px 1px rgba(0,0,0,.3)}
.chart-card{left:534px;top:163px;width:284px;height:188px;background:#fff;border-radius:4px;box-shadow:0 2px 6px rgba(0,0,0,.2);padding:9px 10px 12px}
.chart-fill{width:100%;height:100%;background:linear-gradient(180deg,var(--chart-light) 0%,var(--chart-blue) 75%,var(--pink) 76%,var(--pink) 100%)}

.tab{top:425px;width:246px;height:37px;border:2px solid var(--pink);border-top:none;display:flex;align-items:center;justify-content:center;font-family:"Questrial",sans-serif;font-size:14px;color:#eee;background:var(--ink)}
.tab.active{background:var(--pink);color:#fff}

.feature{top:520px;width:170px;text-align:center}
.feature-ring{display:block;margin:0 auto}
.feature-title{margin:20px auto 0;display:inline-block;font-family:"Questrial",sans-serif;font-size:24px;color:#3d3d3f;letter-spacing:.5px;border-bottom:1px solid #8a8a8a;padding:0 2px 2px}
.feature-link{display:block;margin-top:5px;font-family:"Open Sans",sans-serif;font-size:13px;color:var(--pink)}

.feature-detail{left:90px;top:795px;width:751px;height:109px;background:linear-gradient(#535355,#4a4a4c 85%,#333 100%);color:#f2f2f2;font-family:"Questrial",sans-serif;font-size:19px;line-height:26px;padding:37px 26px 0 31px}
.pointer{left:151px;top:777px}

.contact-bar{left:89px;top:927px;width:748px;height:55px;background:#e8e8e9;border-radius:2px}
.contact-field{left:103px;top:936px;width:721px;height:39px;background:#fff;box-shadow:0 1px 2px rgba(0,0,0,.12);font-family:"Open Sans",sans-serif;font-size:14px;color:#222;padding:10px 9px}
.contact-btn{left:705px;top:939px;width:77px;height:31px;background:var(--green);color:#fff;font-weight:600;font-size:15px;display:flex;align-items:center;justify-content:center;border-radius:1px}

.footer-rule{left:0;top:1002px;width:941px;height:4px;background:var(--pink)}
.site-footer{left:0;top:1006px;width:951px;height:194px;background:var(--footer)}
.footer-head{font-size:15px;font-weight:600;color:#fff}
.footer-col{font-family:"Open Sans",sans-serif;font-size:9.5px;line-height:19px;color:#c8c8c8}
.footer-col b{color:#fff;font-weight:600}
.social{display:grid;grid-template-columns:repeat(4,26px);gap:9px}
.social span{width:26px;height:26px;border-radius:50%;background:#fff;display:block}
.copyright{left:127px;top:1182px;font-family:"Open Sans",sans-serif;font-size:8.5px;color:#fff}
</style>
</head>
<body>
<div class="page">

  <header class="site-header abs"></header>
  <div class="brand abs"><span class="brand-dot"></span>BRIVOLANE</div>
  <nav class="main-nav abs">
    <a class="active" href="#">home</a>
    <a href="#">register</a>
    <a href="#">contact</a>
    <a class="faded" href="#">login</a>
  </nav>

  <section class="hero abs"></section>
  <h1 class="hero-title abs">Brivolane Boosts Company’s Performance</h1>
  <p class="hero-copy abs">Our ERM tool creates an HR engagement cycle to encourage line managers to take initiatives and to enhance the engagement of their team members.Our ERM tool creates an HR engagement cycle to encourage line managers to take initiatives and to enhance the engagement of their team members.</p>
  <div class="cta abs">LET’S GET STARTED!</div>

  <div class="chart-card abs">
    <div class="chart-fill" role="img" aria-label="Illustration of a rising performance chart with conversion and bounce rate highlights and a caption banner"></div>
  </div>

  <div class="tab active abs" style="left:88px">What is Brivolane?</div>
  <div class="tab abs" style="left:345px">How does we work?</div>
  <div class="tab abs" style="left:602px">Why choose Brivolane?</div>

  <div class="feature abs" style="left:82px">
    <svg class="feature-ring" width="166" height="166" viewBox="0 0 166 166" aria-hidden="true">
      <circle cx="83" cy="83" r="83" fill="var(--pink)"/><circle cx="83" cy="83" r="73" fill="var(--ink)"/>
      <g fill="none" stroke="#eee" stroke-width="4">
        <circle cx="66" cy="80" r="29"/><ellipse cx="66" cy="80" rx="13" ry="29"/>
        <path d="M37 80h58M41 66h50M41 94h50M66 51v58"/>
        <circle cx="89" cy="78" r="16" fill="var(--ink)" stroke-width="5"/>
        <path d="M101 90l19 16" stroke-width="8" stroke-linecap="round"/>
      </g>
    </svg>
    <div class="feature-title">EVALUATION</div>
    <span class="feature-link">View More</span>
  </div>
  <div class="feature abs" style="left:281px">
    <svg class="feature-ring" width="166" height="166" viewBox="0 0 166 166" aria-hidden="true">
      <circle cx="83" cy="83" r="83" fill="var(--pink)"/><circle cx="83" cy="83" r="73" fill="var(--ink)"/>
      <g stroke="#eee" stroke-width="4" stroke-linecap="round" fill="#eee">
        <path d="M43 50v68M63 50v68M83 50v68M103 50v68M123 50v68"/>
        <circle cx="43" cy="98" r="6"/><circle cx="63" cy="78" r="6"/><circle cx="83" cy="102" r="6"/><circle cx="103" cy="68" r="6"/><circle cx="123" cy="88" r="6"/>
      </g>
    </svg>
    <div class="feature-title">STRATEGY</div>
    <span class="feature-link">View More</span>
  </div>
  <div class="feature abs" style="left:486px">
    <svg class="feature-ring" width="166" height="166" viewBox="0 0 166 166" aria-hidden="true">
      <circle cx="83" cy="83" r="83" fill="var(--pink)"/><circle cx="83" cy="83" r="73" fill="var(--ink)"/>
      <circle cx="83" cy="83" r="44" fill="none" stroke="#eee" stroke-width="5"/>
      <path d="M83 48v38l-15 18" fill="none" stroke="#eee" stroke-width="5" stroke-linecap="round"/>
    </svg>
    <div class="feature-title">PROCESS</div>
    <span class="feature-link">View More</span>
  </div>
  <div class="feature abs" style="left:684px">
    <svg class="feature-ring" width="166" height="166" viewBox="0 0 166 166" aria-hidden="true">
      <circle cx="83" cy="83" r="83" fill="var(--pink)"/><circle cx="83" cy="83" r="73" fill="var(--ink)"/>
      <circle cx="83" cy="83" r="46" fill="#eee"/>
      <g stroke="var(--ink)" stroke-width="2.2">
        <path d="M83 37v92M37 83h92M50 50l66 66M116 50l-66 66M65 40l36 86M101 40l-36 86M40 65l86 36M40 101l86-36"/>
        <path d="M74 38l18 90M92 38l-18 90M38 74l90 18M38 92l90-18M57 45l52 76M109 45l-52 76M45 57l76 52M45 109l76-52"/>
      </g>
      <circle cx="83" cy="83" r="6" fill="var(--ink)"/>
    </svg>
    <div class="feature-title">IMPACT</div>
    <span class="feature-link">View More</span>
  </div>

  <svg class="pointer abs" width="20" height="19" viewBox="0 0 20 19" aria-hidden="true"><path d="M10 0L20 19H0Z" fill="#535355"/></svg>
  <div class="feature-detail abs">Our ERM tool creates an HR engagement cycle to encourage line managers to take initiatives and to enhance the engagement of their team members.</div>

  <div class="contact-bar abs"></div>
  <div class="contact-field abs">Boost you company’s Performance....</div>
  <div class="contact-btn abs">Contact</div>

  <div class="footer-rule abs"></div>
  <footer class="site-footer abs"></footer>

  <div class="abs" style="left:131px;top:1021px">
    <div class="footer-head">Contact us</div>
    <div class="footer-col" style="margin-top:10px;line-height:20.5px;font-size:10.5px">
      <div><b>Call</b>&nbsp;&nbsp; 123-456-7890</div>
      <div><b>Email</b> hello@brivolane.eu</div>
      <div><b>Skype</b> Brivolane HQ</div>
    </div>
  </div>
  <div class="abs" style="left:313px;top:1021px">
    <div class="footer-head">Follow Us</div>
    <div class="social" style="margin-top:16px;margin-left:-4px"><span></span><span></span><span></span><span></span><span></span><span></span><span></span><span></span></div>
  </div>
  <div class="abs" style="left:547px;top:1018px">
    <div class="footer-head">Company</div>
    <div class="footer-col" style="margin-top:2px">Customer Support<br>FAQ’s<br>Contact Us<br>Blog</div>
  </div>
  <div class="abs" style="left:737px;top:1018px">
    <div class="footer-head" style="font-size:12.5px">Location</div>
    <div class="footer-col" style="margin-top:2px">123, street name<br>landmark,<br>California 123<br>Tel: 123-456-7890<br>Fax. +123-456-7890</div>
  </div>
  <div class="copyright abs">Copyright © 2012 Brivolane.</div>

</div>
</body>
</html>
```